Cleaning Company needs a new business card design

Hi, We are looking for new business card designs to update with our latest logo and company information.
We would like to see designs using the colours:
Royal Blue #4169E1 - this is our company colour so this has to be in there. Please feel free to experiment with other colours.
Must include:
Front of business card:
Logo
Back of the business card:
0800 519 2867
07946 581 302
Email: info@pelvormaids.co.uk
Web: www.pelvormaids.co.uk
Services:
End of Tenancy
Carpet & Upholstery
Regular & One Off
all work fully insured.
The front of the business card with the logo can be made to look raised print. The blue man to be a shiny finish.
The business card needs to be presented in a matt finish
The business must be in the following styles:
Standard Square with rounded corners.
Thank you to all that take part in this.
Target Market(s)
Men and Women of different ages in the UK.
Industry/Entity Type
House Cleaning
Contact Information for Business Card
Front of business card:
Logo
0800 519 2867
07946 581 302
Email: pelvormaids@brimmail.co.uk
Services:
End of Tenancy
Carpet & Upholstery
Regular & One Off
all work fully insured.

```html
<!DOCTYPE html>
<html lang="en">
<head>
<meta charset="utf-8">
<title>Pelvor Maids – Business Card</title>
<link rel="stylesheet" href="https://fonts.googleapis.com/css2?family=Open+Sans:wght@400;600&family=Poppins:wght@600&display=swap">
<style>
  :root {
    --backdrop: #2e2f31;
    --card: #050505;
    --royal: #4169e1;
    --sky: #29a8e0;
    --ink: #ffffff;
  }
  * { box-sizing: border-box; margin: 0; padding: 0; }
  html, body {
    width: 1200px; height: 900px; overflow: hidden;
    background: var(--backdrop);
  }
  .canvas { position: relative; width: 1200px; height: 900px; }
  .card {
    position: absolute;
    width: 620px; height: 354px;
    background: var(--card);
    border-radius: 22px;
    box-shadow: 0 14px 30px rgba(0,0,0,.45);
    overflow: hidden;
  }
  .card-front { left: 110px; top: 100px; }
  .card-back  { left: 470px; top: 480px; }

  .brand {
    position: absolute; inset: 0;
    display: flex; align-items: center; justify-content: center; gap: 16px;
  }
  .brand-dot {
    width: 34px; height: 34px; border-radius: 50%;
    background: var(--royal);
  }
  .brand-name {
    font-family: "Poppins", sans-serif;
    font-weight: 600;
    font-size: 46px;
    color: var(--royal);
    letter-spacing: -0.5px;
  }

  .back-mark {
    position: absolute; right: 40px; top: 40px;
    display: flex; align-items: center; gap: 10px;
  }
  .back-mark .brand-dot { width: 26px; height: 26px; background: var(--sky); }
  .back-mark .brand-name { font-size: 26px; color: var(--sky); }

  .details {
    position: absolute; left: 44px; bottom: 30px;
    font-family: "Open Sans", sans-serif;
    color: var(--ink);
    font-size: 17px; line-height: 1.3;
  }
  .services-title {
    color: var(--sky); font-weight: 400; font-size: 18px;
  }
  .services-list { list-style: none; margin-bottom: 8px; }
  .services-list li { display: flex; align-items: center; gap: 9px; font-weight: 600; }
  .services-list li::before {
    content: ""; width: 9px; height: 9px; border-radius: 50%;
    background: var(--sky); flex: none;
  }
  .contact-list { list-style: none; }
  .contact-list li { display: flex; align-items: center; gap: 10px; font-weight: 600; }
  .contact-list svg {
    width: 13px; height: 13px; flex: none;
    fill: none; stroke: var(--sky); stroke-width: 2;
  }
</style>
</head>
<body>
<main class="canvas">
  <section class="card card-front" aria-label="Card front">
    <div class="brand">
      <span class="brand-dot"></span>
      <span class="brand-name">Pelvor Maids Limited</span>
    </div>
  </section>

  <section class="card card-back" aria-label="Card back">
    <div class="back-mark">
      <span class="brand-dot"></span>
      <span class="brand-name">Pelvor Maids</span>
    </div>

    <div class="details">
      <p class="services-title">SERVICES:</p>
      <ul class="services-list">
        <li>End of Tenancy</li>
        <li>Carpet &amp; Upholstery</li>
        <li>Regular &amp; One Off</li>
      </ul>
      <ul class="contact-list">
        <li>
          <svg viewBox="0 0 16 16" aria-hidden="true"><path d="M3 2l3 0 1 4-2 1a8 8 0 0 0 4 4l1-2 4 1 0 3a2 2 0 0 1-2 1C7 14 2 9 2 4a2 2 0 0 1 1-2z"/></svg>
          0800 519 2867
        </li>
        <li>
          <svg viewBox="0 0 16 16" aria-hidden="true"><rect x="4" y="1.5" width="8" height="13" rx="1.5"/><line x1="7" y1="12" x2="9" y2="12"/></svg>
          07946 581 302
        </li>
        <li>
          <svg viewBox="0 0 16 16" aria-hidden="true"><rect x="1.5" y="3.5" width="13" height="9" rx="1"/><polyline points="1.5,4 8,9 14.5,4"/></svg>
          pelvormaids@brimmail.co.uk
        </li>
        <li>
          <svg viewBox="0 0 16 16" aria-hidden="true"><circle cx="8" cy="8" r="6.5"/><ellipse cx="8" cy="8" rx="3" ry="6.5"/><line x1="1.5" y1="8" x2="14.5" y2="8"/></svg>
          www.pelvormaids.co.uk
        </li>
      </ul>
    </div>
  </section>
</main>
</body>
</html>
```